Kestin Power Battery advertisment for Facebook ads

Objective:
Design a compelling Facebook advertisement to promote the new Federal Government Home Battery Subsidy, encouraging existing solar customers to act now and install a battery system under the new subsidy program.

Key Message:

25kWh Battery System Installed from $9,800
Act now and secure your affordable energy future today!
Design Requirements:

Bold headline showcasing the 25kWh for $9,800 offer.
Clear reference to the Federal Government Battery Subsidy as the reason for the low pricing.
Include messaging around:
Claim your subsidy before it winds down—like the solar rebate, it reduces each year
The subsidy can only be claimed once per household—go large now to future-proof your energy needs
Add a strong Call to Action like: “Beat the Rush—Secure Your Battery Today!”

Target Market(s)

Home owners who want to add batteries to existing solar systems

Industry/Entity Type

Renewable energy

Colors
0054AA
0677BA
7BADD7
CADEEF
E8F1F8
EB3D1F
EC4F4E
F09395
F8D3D4
FCEDEE

Requirements
Must have
• Visual Style: Modern, clean, and high-trust Use imagery of solar homes, battery units, or families enjoying power security at night Include visual cues of savings, energy independence, or clean energy Mobile-optimized, designed for Facebook feed
Nice to have
• Tone: Confident, future-focused, and urgent—while remaining trustworthy and informative. I would like a picture of battery ideally VOM battery on a home or such
Should not have
• must be professional and be a call to action

```html
<!DOCTYPE html>
<html lang="en">
<head>
<meta charset="utf-8">
<title>Home Battery Subsidy – 25kWh Battery System Ad</title>
<link href="https://fonts.googleapis.com/css2?family=Montserrat:wght@300;400;500;700;800;900&display=swap" rel="stylesheet">
<style>
  :root {
    --stage: #b9b9bb;
    --sky-top: #00b1ec;
    --sky-mid: #4cc3d6;
    --mint: #b5e2d9;
    --white: #ffffff;
    --ink: #111111;
    --text: #222a30;
    --green: #6cbf4a;
    --blue: #1fa6de;
    --sun-yellow: #f1e23a;
    --sun-orange: #e98a2c;
    --battery-shade: #c9cccf;
  }
  * { box-sizing: border-box; margin: 0; padding: 0; }
  html, body { width: 1200px; height: 849px; overflow: hidden; }
  body {
    background: var(--stage);
    font-family: "Montserrat", sans-serif;
    position: relative;
  }
  .ad {
    position: absolute;
    left: 220px; top: 55px;
    width: 754px; height: 750px;
    background: var(--white);
    overflow: hidden;
  }
  .ad__sky {
    position: absolute; inset: 0 0 auto 0; height: 380px;
    background: linear-gradient(180deg, var(--sky-top) 0%, var(--sky-top) 22%, var(--sky-mid) 50%, var(--mint) 78%, var(--white) 100%);
  }
  .ad__art { position: absolute; inset: 0; }
  .headline {
    position: absolute; left: 45px; top: 62px;
    color: var(--white);
    font-weight: 800; font-size: 50.5px; line-height: 59px; letter-spacing: -0.3px;
  }
  .price {
    position: absolute; left: 42px; top: 194px;
    color: var(--white);
    font-weight: 300; font-size: 38px; line-height: 46px; white-space: nowrap;
  }
  .price strong { font-weight: 800; position: relative; }
  .price strong::after {
    content: ""; position: absolute; left: 0; right: -2px; bottom: -6px; height: 3px;
    background: linear-gradient(90deg, var(--sun-yellow), var(--sun-orange), #e8462b);
  }
  .subsidy-ref {
    position: absolute; left: 54px; top: 254px;
    color: var(--text); font-weight: 500; font-size: 20.5px; line-height: 25px;
    padding-bottom: 6px; padding-right: 12px;
    border-bottom: 3px solid; border-image: linear-gradient(90deg, var(--green), var(--blue)) 1;
  }
  .alert {
    position: absolute; left: 42px; top: 342px; width: 366px; height: 80px;
  }
  .alert svg { position: absolute; inset: 0; overflow: visible; }
  .alert__text {
    position: absolute; left: 94px; top: 8px;
    color: var(--text); font-size: 16.5px; font-weight: 300; line-height: 20px;
  }
  .alert__text strong { font-weight: 800; color: var(--ink); }
  .once {
    position: absolute; left: 73px; top: 450px;
    color: var(--text); font-size: 18.5px; font-weight: 400; line-height: 26px;
  }
  .once strong { display: block; font-weight: 900; color: var(--ink); }
  .cta {
    position: absolute; left: 0; right: 0; top: 618px;
    text-align: center; color: var(--ink);
    font-weight: 900; font-size: 30.5px; line-height: 37px;
  }
</style>
</head>
<body>
  <main class="ad" aria-label="Home battery subsidy advertisement">
    <div class="ad__sky"></div>

    <svg class="ad__art" width="754" height="750" viewBox="0 0 754 750">
      <defs>
        <linearGradient id="sunPanels" x1="0" y1="1" x2="1" y2="0">
          <stop offset="0" stop-color="#f2e24a"/>
          <stop offset="0.45" stop-color="#e9a93a"/>
          <stop offset="1" stop-color="#e37d3c"/>
        </linearGradient>
        <linearGradient id="boltTail" x1="0" y1="1" x2="1" y2="0">
          <stop offset="0" stop-color="#f1e23a"/>
          <stop offset="1" stop-color="#ecd23a"/>
        </linearGradient>
        <linearGradient id="batteryBody" x1="0" y1="0" x2="1" y2="0">
          <stop offset="0" stop-color="#eef0f1"/>
          <stop offset="0.8" stop-color="#f7f8f8"/>
          <stop offset="0.82" stop-color="#c7cbce"/>
          <stop offset="1" stop-color="#9ea3a7"/>
        </linearGradient>
      </defs>
      <g role="img" aria-label="Rooftop solar panels under warm sunlight">
        <polygon points="612,0 754,0 754,266 665,358 600,330 540,275 476,258 472,248 478,236" fill="url(#sunPanels)"/>
      </g>
      <polygon points="754,58 697,128 701,147 754,149" fill="var(--sky-top)"/>
      <polygon points="499,497 429,606 499,537" fill="url(#boltTail)"/>
      <g role="img" aria-label="Stacked home battery unit">
        <rect x="499" y="280" width="167" height="284" rx="3" fill="url(#batteryBody)"/>
        <rect x="506" y="564" width="152" height="20" rx="2" fill="var(--battery-shade)"/>
      </g>
    </svg>

    <h1 class="headline">25kWh<br>Battery System</h1>
    <p class="price">Installed from <strong>$9,800</strong></p>
    <p class="subsidy-ref">By The Federal<br>Government Battery Subsidy</p>

    <div class="alert">
      <svg width="366" height="80" viewBox="0 0 366 80">
        <defs>
          <linearGradient id="alertStroke" x1="0" y1="0" x2="1" y2="0">
            <stop offset="0" stop-color="#6cbf4a"/>
            <stop offset="1" stop-color="#1fa6de"/>
          </linearGradient>
          <linearGradient id="bang" x1="0" y1="0" x2="0" y2="1">
            <stop offset="0" stop-color="#8cc63f"/>
            <stop offset="1" stop-color="#39b0c8"/>
          </linearGradient>
        </defs>
        <path d="M41 1 H326 A39 39 0 0 1 326 79 H41" fill="var(--white)" stroke="url(#alertStroke)" stroke-width="2"/>
        <circle cx="41" cy="40" r="39" fill="var(--white)" stroke="url(#alertStroke)" stroke-width="2"/>
        <path d="M34 16 H47 L43 51 H38 Z" fill="url(#bang)"/>
        <circle cx="40.5" cy="60" r="6.5" fill="url(#bang)"/>
      </svg>
      <p class="alert__text">Claim your subsidy before it<br>winds down—<strong>like the solar<br>rebate, it reduces each year</strong></p>
    </div>

    <p class="once">The subsidy can only be claimed<br>once per household—<strong>go large now to future-proof<br>your energy needs.</strong></p>

    <p class="cta">Beat the Rush —<br>Secure Your Battery Today!</p>
  </main>
</body>
</html>
```